Business Card Design

I already have a company logo for my company. I have a logo for the manufacturer we represent. I want a professional business card design.

```html
<!DOCTYPE html>
<html lang="en">
<head>
<meta charset="utf-8">
<title>Beacon Guard Co — Business Card</title>
<link href="https://fonts.googleapis.com/css2?family=Exo+2:wght@400;500;700&display=swap" rel="stylesheet">
<style>
  :root {
    --backdrop: #2b2d31;
    --paper: #ffffff;
    --gold: #8f7012;
    --gold-light: #a8861a;
    --gold-dark: #5e4a0e;
    --red: #e8262c;
    --ink: #3a3a3a;
    --muted: #555555;
  }
  * { box-sizing: border-box; margin: 0; padding: 0; }
  html, body { width: 1200px; height: 900px; overflow: hidden; }
  body {
    background: var(--backdrop);
    font-family: "Exo 2", Arial, sans-serif;
    position: relative;
  }
  .card {
    position: absolute;
    left: 320px;
    width: 560px;
    height: 320px;
    border-radius: 22px;
    overflow: hidden;
  }
  .card--front { top: 100px; background: var(--paper); }
  .card--back {
    top: 480px;
    background: radial-gradient(ellipse at 70% 80%, var(--gold-light) 0%, var(--gold) 45%, var(--gold-dark) 100%);
  }

  .wordmark {
    position: absolute;
    display: flex;
    align-items: center;
    gap: 12px;
    font-weight: 700;
    letter-spacing: 2px;
    text-transform: uppercase;
  }
  .wordmark__square { width: 26px; height: 26px; }
  .card--front .wordmark {
    top: 46px; left: 0; right: 0; justify-content: center;
    font-size: 34px; color: var(--red);
  }
  .card--front .wordmark__square { background: var(--gold); }
  .card--back .wordmark {
    top: 0; bottom: 0; left: 0; right: 0; justify-content: center;
    font-size: 42px; color: var(--paper);
  }
  .card--back .wordmark__square { background: var(--red); width: 32px; height: 32px; }

  .front__rule {
    position: absolute; top: 100px; left: 150px; width: 260px; height: 3px;
    background: var(--gold);
  }

  .person {
    position: absolute; top: 150px; left: 48px; width: 210px;
  }
  .person__name { color: var(--red); font-size: 27px; font-weight: 500; line-height: 1.1; }
  .person__title { color: var(--muted); font-size: 15px; margin-top: 4px; }

  .divider {
    position: absolute; top: 150px; left: 268px; width: 2px; height: 82px;
    background: var(--gold);
  }

  .contacts {
    position: absolute; top: 150px; left: 286px;
    list-style: none;
    color: var(--ink); font-size: 16px; line-height: 27px;
  }
  .contacts li { display: flex; align-items: center; gap: 9px; }
  .contacts svg { width: 13px; height: 13px; flex: none; }

  .address-band {
    position: absolute; left: 0; right: 0; bottom: 0; height: 48px;
    background: var(--gold);
    color: #f3e6b8; font-size: 16px;
    display: flex; align-items: center; padding-left: 48px;
  }
</style>
</head>
<body>

<section class="card card--front" aria-label="Business card front">
  <div class="wordmark"><span class="wordmark__square"></span>Beacon Guard Co</div>
  <div class="front__rule"></div>

  <div class="person">
    <p class="person__name">Dana Whitfield</p>
    <p class="person__title">Managing Director</p>
  </div>

  <div class="divider"></div>

  <ul class="contacts">
    <li>
      <svg viewBox="0 0 16 16" aria-hidden="true"><circle cx="8" cy="8" r="8" fill="#e8262c"/><path d="M5 4.5l1.6-.4.8 2-1 .7a5 5 0 0 0 2.8 2.8l.7-1 2 .8-.4 1.6c-3.4.3-6.8-3.1-6.5-6.5z" fill="#fff"/></svg>
      555.210.4870
    </li>
    <li>
      <svg viewBox="0 0 16 16" aria-hidden="true"><circle cx="8" cy="8" r="8" fill="#e8262c"/><rect x="4" y="5.2" width="8" height="5.6" fill="#fff"/><path d="M4 5.2l4 3 4-3" fill="none" stroke="#e8262c" stroke-width="0.9"/></svg>
      hello@beaconguardco.com
    </li>
    <li>
      <svg viewBox="0 0 16 16" aria-hidden="true"><circle cx="8" cy="8" r="8" fill="#e8262c"/><circle cx="8" cy="8" r="4" fill="none" stroke="#fff" stroke-width="1"/><path d="M4 8h8M8 4c-1.6 2.4-1.6 5.6 0 8M8 4c1.6 2.4 1.6 5.6 0 8" fill="none" stroke="#fff" stroke-width="0.8"/></svg>
      www.beaconguardco.com
    </li>
  </ul>

  <div class="address-band">240 Alder Ave. Riverton, CO 80000</div>
</section>

<section class="card card--back" aria-label="Business card back">
  <div class="wordmark"><span class="wordmark__square"></span>Beacon Guard Co</div>
</section>

</body>
</html>
```